Business Card Design Project

i have the logo designed.
I require designs for the managing director and the general manager.
we need space for email, and a mobile number.
any other cool stuff/design you guys just let me see what you got.
The managing director card could be black, minimalist, and the cards for the rest of the company could be using the green logo.
it has to impress. transportation market is fragmented, we want to appear professional and sophisticated.
Md: Tarek bani rahim
General manager: omer rahim
clients: procurement heads of contracting companies
Business

```html
<!DOCTYPE html>
<html lang="en">
<head>
<meta charset="utf-8">
<title>Stridelane – Managing Director Business Card</title>
<link rel="stylesheet" href="https://fonts.googleapis.com/css2?family=Open+Sans:wght@400;600;700&display=swap">
<style>
  :root {
    --stage: #1c1c1c;
    --card-dark: #050505;
    --card-light: #1b1b1b;
    --ink: #ffffff;
    --ink-soft: #d6d6d6;
    --accent: #a4cc3a;
  }
  * { margin: 0; padding: 0; box-sizing: border-box; }
  html, body {
    width: 1200px;
    height: 900px;
    overflow: hidden;
    background: var(--stage);
    font-family: "Open Sans", Arial, sans-serif;
  }
  .card {
    position: absolute;
    top: 300px;
    width: 525px;
    height: 300px;
    background: radial-gradient(ellipse at 60% 35%, var(--card-light) 0%, #0c0c0c 55%, var(--card-dark) 100%);
    box-shadow: 0 8px 24px rgba(0,0,0,0.6);
    color: var(--ink);
  }
  .card--front { left: 48px; }
  .card--back { left: 608px; }

  .wordmark {
    position: absolute;
    display: flex;
    align-items: center;
    gap: 14px;
    font-weight: 700;
    color: var(--ink);
    letter-spacing: 0.5px;
    line-height: 1;
  }
  .wordmark__dot {
    border-radius: 50%;
    background: var(--ink);
  }
  .card--front .wordmark {
    left: 150px;
    top: 152px;
    font-size: 44px;
  }
  .card--front .wordmark__dot { width: 22px; height: 22px; }

  .card--back .wordmark {
    left: 330px;
    top: 228px;
    font-size: 20px;
    gap: 7px;
  }
  .card--back .wordmark__dot { width: 10px; height: 10px; }

  .holder {
    position: absolute;
    left: 87px;
    top: 78px;
  }
  .holder__name {
    font-size: 11.5px;
    font-weight: 700;
    letter-spacing: 0.3px;
    text-transform: uppercase;
  }
  .holder__title {
    margin-top: 3px;
    font-size: 8.5px;
    font-weight: 600;
    letter-spacing: 0.3px;
    color: var(--ink-soft);
    text-transform: uppercase;
  }
  .contacts {
    position: absolute;
    left: 63px;
    top: 118px;
    list-style: none;
  }
  .contacts__item {
    display: flex;
    align-items: center;
    gap: 15px;
    margin-bottom: 6px;
    font-size: 9.5px;
    color: var(--ink-soft);
  }
  .contacts__item svg { width: 10px; height: 10px; flex: none; }
  .contacts__phones { font-size: 7.5px; line-height: 1.4; letter-spacing: 0.3px; }
</style>
</head>
<body>

<section class="card card--front" aria-label="Card front">
  <div class="wordmark"><span class="wordmark__dot"></span>Stridelane</div>
</section>

<section class="card card--back" aria-label="Card back">
  <div class="holder">
    <p class="holder__name">Tarek bani rahim</p>
    <p class="holder__title">Managing Director</p>
  </div>
  <ul class="contacts">
    <li class="contacts__item">
      <svg viewBox="0 0 10 10" aria-hidden="true"><rect x="2.5" y="0.5" width="5" height="9" rx="1" fill="none" stroke="var(--accent)" stroke-width="1"/><circle cx="5" cy="7.8" r="0.6" fill="var(--accent)"/></svg>
      <span class="contacts__phones">XX XXXX XXXX<br>XXX XXX XXXX</span>
    </li>
    <li class="contacts__item">
      <svg viewBox="0 0 10 10" aria-hidden="true"><rect x="0.5" y="2" width="9" height="6" fill="var(--accent)"/><path d="M0.5 2 L5 5.5 L9.5 2" fill="none" stroke="#111" stroke-width="0.8"/></svg>
      <span>tarekbanirahim@stridelane.au</span>
    </li>
    <li class="contacts__item">
      <svg viewBox="0 0 10 10" aria-hidden="true"><circle cx="5" cy="5" r="4.5" fill="var(--accent)"/><path d="M0.5 5 H9.5 M5 0.5 C2.5 3 2.5 7 5 9.5 M5 0.5 C7.5 3 7.5 7 5 9.5" fill="none" stroke="#111" stroke-width="0.6"/></svg>
      <span>www.stridelane.com</span>
    </li>
  </ul>
  <div class="wordmark"><span class="wordmark__dot"></span>Stridelane</div>
</section>

</body>
</html>
```